Vardek Hub, LLC. is the name of the company that will be an Internet startup working in E-commerce and

We are a new company and going to start the business by hiring people we need. We are on “Hiring Now…” status right now which we like to be displayed on the website homepage.
The website should allow us to start the hiring process with letting people see and apply for jobs posted on the website.

the Brightfold is attached.

Target Market(s)

Tech Job Seekers, Programmers, iOS and Android Developers, Software engineers, Graphic designers, QA engineers, Customer Service Reps,...

Industry/Entity Type

Internet

Number of Pages Required

5+ page

Font styles to use
Serif
Sans Serif

Colors

Designer to choose colors to be used in the design.

Requirements
Must have
• We need a system to help job seekers to upload the resume and cover letter and fill the required forms and answer some questions on a form designed to evaluate the job seekers and let them know if they fit in the position and should apply for it.
• We also want job seekers to do a Pre-Employment Tests including Aptitude, Personality, and Skills after they qualified for a job which links our website to web-based pre-employment testing services websites like (Quorva, Pellmark, Brumhall & Associates, Tolvin Assessment, …)

```html
<!DOCTYPE html>
<html lang="en">
<head>
<meta charset="utf-8">
<title>Vardek Hub — Hiring Now</title>
<link href="https://fonts.googleapis.com/css2?family=Roboto:wght@400;500;700&family=Roboto+Slab:wght@400;500&display=swap" rel="stylesheet">
<style>
:root{
  --orange:#f8560f;
  --blue:#2f8cc6;
  --blue-band:#3a92c8;
  --ink:#333;
  --muted:#777;
  --light:#f4f6f8;
  --white:#fff;
  --footer:#343434;
  --line:#e3e3e3;
}
*{box-sizing:border-box;margin:0;padding:0}
html,body{width:1200px;height:2817px;overflow:hidden}
body{position:relative;background:var(--white);font-family:'Roboto',Arial,sans-serif;color:var(--ink)}
.abs{position:absolute}
.center{left:0;width:1200px;text-align:center}
.slab{font-family:'Roboto Slab',Georgia,serif}
/* header */
.header{top:0;left:0;width:1200px;height:84px;background:var(--white)}
.brand{left:85px;top:18px;display:flex;align-items:center;gap:10px;font-size:34px;font-weight:700;color:var(--blue);letter-spacing:1px}
.brand i{display:block;width:14px;height:14px;border-radius:50%;background:var(--orange)}
.nav a{position:absolute;top:36px;font-size:12px;color:#555;text-decoration:none;text-transform:uppercase}
.nav a.active{color:var(--blue)}
.btn-hiring{left:993px;top:23px;width:119px;height:43px;background:var(--orange);color:#fff;font-family:'Roboto Slab',serif;font-size:17px;line-height:43px;text-align:center}
/* hero */
.hero{top:84px;left:0;width:1200px;height:504px;background:linear-gradient(120deg,#5a5550 0%,#3c3a38 45%,#2c2d30 100%)}
.hero-title{top:296px;font-size:44px;font-weight:500;color:#fff}
.hero-panel{left:265px;top:357px;width:668px;height:159px;background:rgba(255,255,255,.22)}
.email{left:295px;top:389px;width:608px;height:47px;background:#fff;font-size:11px;color:#666;line-height:47px;padding-left:22px}
.hero-btn{top:451px;height:47px;line-height:47px;font-size:13px;color:#fff;text-align:center}
/* sections */
.sec-title{font-family:'Roboto Slab',serif;font-size:27px;color:var(--orange)}
.sec-sub{font-size:11px;color:var(--muted)}
.service{width:240px;text-align:center}
.service .ring{width:112px;height:112px;margin:0 auto;border-radius:50%;border:5px solid var(--blue);box-shadow:inset 0 0 0 4px #fff,inset 0 0 0 8px var(--orange);display:flex;align-items:center;justify-content:center}
.service h3{margin-top:15px;font-family:'Roboto Slab',serif;font-weight:400;font-size:19px;color:var(--orange)}
.service p{margin-top:14px;font-size:11px;line-height:22px;color:var(--muted)}
.btn{height:51px;line-height:51px;width:190px;left:505px;color:#fff;text-align:center;font-family:'Roboto Slab',serif;font-size:18px}
.jobs-bg{top:1046px;left:0;width:1200px;height:554px;background:var(--light)}
.job-card{width:490px;height:130px;background:#fff;border:1px solid var(--line)}
.job-card .co{position:absolute;left:0;top:0;width:135px;height:130px;display:flex;align-items:center;justify-content:center;font-size:17px;font-weight:500}
.job-card .divider{position:absolute;left:135px;top:22px;width:1px;height:86px;background:var(--line)}
.job-card h4{position:absolute;left:155px;top:22px;font-family:'Roboto Slab',serif;font-weight:400;font-size:15px;color:#555}
.job-card .loc{position:absolute;left:155px;top:52px;font-size:11px;color:var(--blue);display:flex;align-items:center;gap:6px}
.job-card .tag{position:absolute;left:155px;top:83px;width:92px;height:33px;line-height:33px;text-align:center;color:#fff;font-family:'Roboto Slab',serif;font-size:13px}
.stats{top:1600px;left:0;width:1200px;height:317px;background:linear-gradient(90deg,#3a8fc6,#3f97cc)}
.stat{width:240px;text-align:center;color:#fff}
.stat .ring{width:114px;height:114px;margin:0 auto;border-radius:50%;border:2px solid rgba(255,255,255,.85);display:flex;align-items:center;justify-content:center}
.stat h5{margin-top:31px;font-size:18px;font-weight:700}
.stat b{display:block;margin-top:8px;font-size:16px;font-weight:500}
.quote{left:238px;top:2008px;width:724px;font-size:11px;line-height:22px;color:var(--muted);text-align:center}
.qmark{font-family:'Roboto Slab',serif;font-size:30px;color:#555}
.face{border-radius:50%;border:4px solid #fff}
.sub-bg{top:2310px;left:0;width:1200px;height:272px;background:var(--light)}
.footer{top:2582px;left:0;width:1200px;height:235px;background:var(--footer)}
.social{width:60px;height:60px;border-radius:50%;border:1px solid #8a8a8a;display:flex;align-items:center;justify-content:center}
.social i{width:6px;height:6px;border-radius:50%;background:#fff}
.foot-nav{top:2712px;display:flex;justify-content:center;gap:0;font-size:11px;color:#ddd}
.foot-nav span{padding:0 28px;border-right:1px solid #888}
.foot-nav span:last-child{border-right:0}
</style>
</head>
<body>

<header class="abs header">
  <div class="abs brand"><span>VARDEK HUB</span><i></i></div>
  <nav class="nav">
    <a class="active" style="left:376px">Home</a>
    <a style="left:460px">About</a>
    <a style="left:550px">Jobs</a>
    <a style="left:630px">Freelancers</a>
    <a style="left:760px">How It Works</a>
    <a style="left:898px">Contact Us</a>
  </nav>
  <div class="abs btn-hiring">Hiring Now</div>
</header>

<section class="abs hero" role="img" aria-label="Photo from above of two business people shaking hands across a desk with papers"></section>
<h1 class="abs center hero-title">WELCOME TO VARDEK HUB</h1>
<div class="abs hero-panel"></div>
<div class="abs email">ENTER YOUR EMAIL :</div>
<div class="abs hero-btn" style="left:441px;width:156px;background:var(--orange)">UPLOAD RESUME</div>
<div class="abs hero-btn" style="left:605px;width:154px;background:var(--blue)">COVER LETTER</div>

<!-- testing services -->
<h2 class="abs center sec-title" style="top:622px">Pre-Employment Testing Services</h2>
<p class="abs center sec-sub" style="top:668px">Sed ut perspiciatis unde omnis iste natus error sit voluptatem accusantium doloremque laudantium, totam rem aperiam</p>

<div class="abs service" style="left:92px;top:723px">
  <div class="ring"><svg width="44" height="44" viewBox="0 0 44 44" fill="none" stroke="#2f8cc6" stroke-width="2.5"><rect x="9" y="7" width="24" height="30" rx="2"/><rect x="16" y="4" width="10" height="6" fill="#2f8cc6"/><path d="M14 17h14M14 23h14M14 29h8"/><circle cx="32" cy="33" r="6" fill="#2f8cc6"/><path d="M29 33l2 2 4-4" stroke="#fff" stroke-width="2"/></svg></div>
  <h3>Quorva</h3>
  <p>Sed ut perspiciatis unde omnis iste natus<br>laudantium totam rem aperiam</p>
</div>
<div class="abs service" style="left:350px;top:723px">
  <div class="ring"><svg width="46" height="46" viewBox="0 0 46 46" fill="#2f8cc6"><circle cx="23" cy="12" r="5"/><path d="M15 24a8 8 0 0 1 16 0z"/><circle cx="11" cy="28" r="4.5"/><path d="M4 39a7 7 0 0 1 14 0z"/><circle cx="35" cy="28" r="4.5"/><path d="M28 39a7 7 0 0 1 14 0z"/></svg></div>
  <h3>Pellmark</h3>
  <p>Sed ut perspiciatis unde omnis iste natus<br>laudantium totam rem aperiam</p>
</div>
<div class="abs service" style="left:609px;top:723px">
  <div class="ring"><svg width="50" height="40" viewBox="0 0 50 40" fill="#2f8cc6"><path d="M2 14l8-8 6 6-8 8z"/><path d="M48 14l-8-8-6 6 8 8z"/><path d="M14 14l9-5h8l9 9-12 12c-2 2-4 2-6 0l-9-9z" fill="none" stroke="#2f8cc6" stroke-width="3"/></svg></div>
  <h3>Brumhall &amp; Associates</h3>
  <p>Sed ut perspiciatis unde omnis iste natus<br>laudantium totam rem aperiam</p>
</div>
<div class="abs service" style="left:866px;top:723px">
  <div class="ring"><svg width="44" height="44" viewBox="0 0 44 44" fill="none" stroke="#2f8cc6" stroke-width="3"><circle cx="19" cy="19" r="12"/><path d="M28 28l10 10" stroke-width="5"/><path d="M13 23v-3M19 23v-7M25 23v-5" stroke-width="2.5"/></svg></div>
  <h3>Tolvin Assessment</h3>
  <p>Sed ut perspiciatis unde omnis iste natus<br>laudantium totam rem aperiam</p>
</div>

<div class="abs btn" style="top:965px;background:var(--orange)">Take The Test</div>

<!-- recent jobs -->
<div class="abs jobs-bg"></div>
<h2 class="abs center sec-title" style="top:1077px">Recent Jobs</h2>
<p class="abs center sec-sub" style="top:1123px">Sed ut perspiciatis unde omnis iste natus error sit voluptatem accusantium doloremque laudantium, totam rem aperiam</p>

<div class="abs job-card" style="left:85px;top:1177px">
  <div class="co" style="color:#c0392b">Lumaro</div><div class="divider"></div>
  <h4>Sed ut perspiciatis unde omnis iste natus</h4>
  <div class="loc"><svg width="9" height="12" viewBox="0 0 9 12"><path d="M4.5 0A4.5 4.5 0 0 0 0 4.5C0 8 4.5 12 4.5 12S9 8 9 4.5A4.5 4.5 0 0 0 4.5 0z" fill="#2f8cc6"/><circle cx="4.5" cy="4.5" r="1.6" fill="#fff"/></svg># 12 Lorem Ipsum Dummy</div>
  <div class="tag" style="background:var(--orange)">Full Time</div>
</div>
<div class="abs job-card" style="left:622px;top:1177px">
  <div class="co" style="color:#555">Quintel</div><div class="divider"></div>
  <h4>Sed ut perspiciatis unde omnis iste natus</h4>
  <div class="loc"><svg width="9" height="12" viewBox="0 0 9 12"><path d="M4.5 0A4.5 4.5 0 0 0 0 4.5C0 8 4.5 12 4.5 12S9 8 9 4.5A4.5 4.5 0 0 0 4.5 0z" fill="#2f8cc6"/><circle cx="4.5" cy="4.5" r="1.6" fill="#fff"/></svg># 12 Lorem Ipsum Dummy</div>
  <div class="tag" style="background:var(--blue)">Part Time</div>
</div>
<div class="abs job-card" style="left:85px;top:1333px">
  <div class="co" style="color:#e8661a">Brightfold</div><div class="divider"></div>
  <h4>Sed ut perspiciatis unde omnis iste natus</h4>
  <div class="loc"><svg width="9" height="12" viewBox="0 0 9 12"><path d="M4.5 0A4.5 4.5 0 0 0 0 4.5C0 8 4.5 12 4.5 12S9 8 9 4.5A4.5 4.5 0 0 0 4.5 0z" fill="#2f8cc6"/><circle cx="4.5" cy="4.5" r="1.6" fill="#fff"/></svg># 12 Lorem Ipsum Dummy</div>
  <div class="tag" style="background:var(--blue)">Part Time</div>
</div>
<div class="abs job-card" style="left:622px;top:1333px">
  <div class="co" style="color:#444">Stonepath</div><div class="divider"></div>
  <h4>Sed ut perspiciatis unde omnis iste natus</h4>
  <div class="loc"><svg width="9" height="12" viewBox="0 0 9 12"><path d="M4.5 0A4.5 4.5 0 0 0 0 4.5C0 8 4.5 12 4.5 12S9 8 9 4.5A4.5 4.5 0 0 0 4.5 0z" fill="#2f8cc6"/><circle cx="4.5" cy="4.5" r="1.6" fill="#fff"/></svg># 12 Lorem Ipsum Dummy</div>
  <div class="tag" style="background:var(--orange)">Full Time</div>
</div>

<div class="abs btn" style="top:1500px;background:var(--blue)">Apply For Jobs</div>

<!-- stats -->
<section class="abs stats"></section>
<div class="abs stat" style="left:92px;top:1671px">
  <div class="ring"><svg width="36" height="28" viewBox="0 0 36 28" fill="none" stroke="#fff" stroke-width="2.5"><rect x="6" y="3" width="24" height="16" rx="1"/><path d="M2 24h32"/></svg></div>
  <h5>JOB POSTED</h5><b>152</b>
</div>
<div class="abs stat" style="left:350px;top:1671px">
  <div class="ring"><svg width="30" height="30" viewBox="0 0 30 30" fill="#fff"><path d="M20 3l7 7-15 15-8 2 2-8z"/></svg></div>
  <h5>COMPANIES</h5><b>1118</b>
</div>
<div class="abs stat" style="left:609px;top:1671px">
  <div class="ring"><svg width="34" height="32" viewBox="0 0 34 32" fill="#fff"><path d="M13 2h8v10h6l-10 10-10-10h6z"/><path d="M2 22h8l3 4h8l3-4h8v8H2z"/></svg></div>
  <h5>POSSITION FILLED</h5><b>258</b>
</div>
<div class="abs stat" style="left:866px;top:1671px">
  <div class="ring"><svg width="40" height="32" viewBox="0 0 40 32" fill="#fff"><circle cx="20" cy="8" r="6"/><path d="M10 28a10 10 0 0 1 20 0z"/><circle cx="8" cy="12" r="4.5"/><path d="M0 28a8 8 0 0 1 10-7v7z"/><circle cx="32" cy="12" r="4.5"/><path d="M40 28a8 8 0 0 0-10-7v7z"/></svg></div>
  <h5>MEMBERS</h5><b>12548</b>
</div>

<!-- testimonials -->
<h2 class="abs center sec-title" style="top:1954px">Our Testimonials</h2>
<span class="abs qmark" style="left:212px;top:1996px">&ldquo;</span>
<p class="abs quote">Sed ut perspiciatis unde omnis iste natus error sit voluptatem accusantium doloremque laudantium, totam rem aperiam, eaque ipsa quae ab illo inventore veritatis et quasi architecto beatae vitae dicta sunt explicabo. Nemo enim ipsam voluptatem quia voluptas sit aspernatur aut odit aut fugit, sed quia consequuntur magni dolores eos qui ratione voluptatem sequi nesciunt.</p>
<span class="abs qmark" style="left:874px;top:2052px">&rdquo;</span>
<div class="abs face" role="img" aria-label="Portrait of a customer" style="left:476px;top:2119px;width:100px;height:100px;background:radial-gradient(circle,#bdbdbd,#6e6e6e)"></div>
<div class="abs face" role="img" aria-label="Portrait of a customer" style="left:624px;top:2119px;width:100px;height:100px;background:radial-gradient(circle,#b5b5b5,#5a5a5a)"></div>
<div class="abs face" role="img" aria-label="Portrait of the featured customer" style="left:547px;top:2112px;width:108px;height:108px;background:radial-gradient(circle,#e2b493,#8a5a3c);z-index:2"></div>
<p class="abs center slab" style="top:2247px;font-size:17px;color:var(--blue)">Name : Edric Vane</p>
<p class="abs center" style="top:2274px;font-size:11px;color:var(--muted)">Posted On 25 Sep 2017</p>

<!-- subscription -->
<div class="abs sub-bg"></div>
<h2 class="abs center sec-title" style="top:2339px">Our Subscription</h2>
<p class="abs center sec-sub" style="top:2395px;left:240px;width:720px;line-height:22px">Sed ut perspiciatis unde omnis iste natus error sit voluptatem accusantium doloremque laudantium, totam rem aperiam, eaque ipsa quae ab illo inventore veritatis et quasi architecto beatae vitae dicta sunt explicabo.</p>
<div class="abs" style="left:284px;top:2471px;width:482px;height:51px;background:#fff;border:1px solid var(--line);font-size:11px;color:#666;line-height:49px;padding-left:16px">Enter Your Email id :</div>
<div class="abs" style="left:766px;top:2471px;width:149px;height:51px;background:var(--blue);color:#fff;font-size:14px;font-weight:700;letter-spacing:1px;line-height:51px;text-align:center">SUBSCRIBE</div>

<!-- footer -->
<footer class="abs footer"></footer>
<div class="abs social" style="left:391px;top:2614px"><i></i></div>
<div class="abs social" style="left:462px;top:2614px"><i></i></div>
<div class="abs social" style="left:533px;top:2614px"><i></i></div>
<div class="abs social" style="left:607px;top:2614px"><i></i></div>
<div class="abs social" style="left:676px;top:2614px"><i></i></div>
<div class="abs social" style="left:749px;top:2614px"><svg width="18" height="14" viewBox="0 0 18 14" fill="none" stroke="#fff" stroke-width="1.6"><rect x="1" y="1" width="16" height="12" rx="1"/><path d="M1 2l8 6 8-6"/></svg></div>
<div class="abs" style="left:280px;top:2689px;width:640px;height:1px;background:#4a4a4a"></div>
<div class="abs center foot-nav"><span>HOME</span><span>ABOUT</span><span>JOBS</span><span>FREELANCERS</span><span>HOW IT WORKS</span><span>CONTACT US</span></div>
<p class="abs center" style="top:2757px;font-size:11px;color:#ddd">© Copyrights 2017 Vardek Hub.All Rights Reserved.</p>

</body>
</html>
```